Business Card Design Project

TRK Solutions is a Electrical and Communications Services and Maintenance contractor to the Mining Oil and Gas sectors of Australia.
Our clients will be planners, Schedulers, Tradespeople and Engineers

We are yet to determine the primary colours that we will use on the business cards but the logos attached will form foundation of the colours used for logos on Business cards, Website, Uniforms, vehicles etc.

Target Market(s)

Mining engineers and shedulers

Industry/Entity Type

Contractor

Requirements
Must have
• information to be included on the card

Name: Derek Hanley
Title: Managing Director
Company: TRK Solutions Pty Ltd
Phone: 08 9YYY YYYY
Mobile 0400 813 942
email: dhanley@trksolutions-example.com
Website www.trksolutions-example.com

Address: U5/7 Bexley Street Kelvale, WA 6111
Postal Address: PO Box 4187 Kelvale WA 6112

Nice to have
• Double sided. Maybe the logo on the back

```html
<!DOCTYPE html>
<html lang="en">
<head>
<meta charset="utf-8">
<title>TRK Solutions – Business Card</title>
<link href="https://fonts.googleapis.com/css2?family=PT+Sans+Narrow:wght@400;700&display=swap" rel="stylesheet">
<style>
  :root {
    --backdrop: #d9d9d9;
    --orange: #ea6e24;
    --orange-light: #f08a3a;
    --orange-ghost: rgba(255, 170, 90, 0.22);
    --navy: #0e1d38;
    --navy-glow: #123056;
    --ink: #14213d;
    --white: #ffffff;
  }
  * { margin: 0; padding: 0; box-sizing: border-box; }
  html, body {
    width: 1200px;
    height: 1200px;
    overflow: hidden;
    background: var(--backdrop);
    font-family: "PT Sans Narrow", "Arial Narrow", sans-serif;
  }
  .canvas { position: relative; width: 1200px; height: 1200px; }

  .card {
    position: absolute;
    left: 181px;
    width: 813px;
    height: 500px;
    overflow: hidden;
  }

  /* Front */
  .card-front {
    top: 80px;
    background: radial-gradient(ellipse at 45% 45%, var(--orange-light) 0%, var(--orange) 75%);
  }
  .front-ghost {
    position: absolute;
    left: 0;
    right: 0;
    top: 150px;
    text-align: center;
    font-size: 130px;
    font-weight: 700;
    line-height: 1;
    color: var(--orange-ghost);
    white-space: nowrap;
  }
  .front-name {
    position: absolute;
    left: 0;
    right: 0;
    top: 218px;
    text-align: center;
    font-size: 72px;
    font-weight: 400;
    color: var(--white);
    line-height: 1;
    letter-spacing: 1px;
  }

  /* Back */
  .card-back {
    top: 599px;
    background: var(--white);
  }
  .back-panel {
    position: absolute;
    left: 0;
    top: 0;
    width: 396px;
    height: 500px;
    background: radial-gradient(ellipse at 20% 50%, var(--navy-glow) 0%, var(--navy) 70%);
  }
  .back-panel-name {
    position: absolute;
    left: 0;
    right: 0;
    top: 228px;
    text-align: center;
    font-size: 40px;
    color: var(--white);
    line-height: 1;
  }
  .back-stripe {
    position: absolute;
    left: 396px;
    top: 0;
    width: 6px;
    height: 500px;
    background: var(--orange);
  }
  .contact {
    position: absolute;
    left: 413px;
    top: 120px;
    color: var(--ink);
    font-size: 24px;
    line-height: 34px;
  }
  .contact p { white-space: nowrap; }
  .contact .person { font-weight: 700; }
  .contact .title { font-weight: 400; }
  .contact .gap { height: 34px; }
  .contact .website { font-weight: 700; font-style: italic; font-size: 25px; }
  .contact .address {
    font-weight: 700;
    font-style: italic;
    font-size: 14px;
    line-height: 21px;
  }
  .contact .address-first { margin-top: 6px; }
</style>
</head>
<body>
<div class="canvas">

  <section class="card card-front" aria-label="Card front">
    <div class="front-ghost" aria-hidden="true">TRK Solutions</div>
    <div class="front-name">TRK Solutions</div>
  </section>

  <section class="card card-back" aria-label="Card back">
    <div class="back-panel">
      <div class="back-panel-name">TRK Solutions</div>
    </div>
    <div class="back-stripe"></div>
    <div class="contact">
      <p><span class="person">Derek Hanley</span> <span class="title">[Managing Director]</span></p>
      <p>TRK Solutions Pty Ltd</p>
      <div class="gap"></div>
      <p>T. 08 9YYY YYYY</p>
      <p>M. 0400 813 942</p>
      <p>dhanley@trksolutions-example.com</p>
      <p class="website">www.trksolutions-example.com</p>
      <p class="address address-first">Address: U5/7 Bexley Street Kelvale, WA 6111</p>
      <p class="address">Postal Address: PO Box 4187 Kelvale WA 6112</p>
    </div>
  </section>

</div>
</body>
</html>
```